Minimalist Planner/Journal Design

We need a planner/journal designed for daily use in a small group. I've attached a requirements document that outlines what every page needs to have on it. I've also attached a basic rough draft that we had made in Canva but the draft needs to be redesigned to look more in line with the style we need. I've attached some sample pages from some planners we like the style of. Feel free to add your own creativity and stylistic choices but keep in mind we are trying to get a very 'clean and minimalist design'. The deliverables should be both a pdf of the 8 planner pages, as well as the photoshop/gimp/illustrator files for the project.

Font styles to use
Other font styles liked:
• You choose, but we prefer thin , basic/minimal font faces

Requirements
Must have
• Minimal Design

```html
<!DOCTYPE html>
<html lang="en">
<head>
<meta charset="utf-8">
<title>Minimalist Planner Pages</title>
<link href="https://fonts.googleapis.com/css2?family=Montserrat:wght@300;400;700;800&family=Roboto:wght@300;400&display=swap" rel="stylesheet">
<style>
:root{
  --backdrop:#6d6d6d;
  --paper:#ffffff;
  --ink:#1c1c1c;
  --soft:#8a8a8a;
  --rule:#d4d4d4;
  --fill:#efefef;
  --fold:#d9d9d9;
}
*{box-sizing:border-box;margin:0;padding:0}
html,body{width:1200px;height:3024px;overflow:hidden;background:var(--backdrop)}
body{position:relative;font-family:"Roboto",Arial,sans-serif;color:var(--ink);font-weight:300}
.page{position:absolute;background:var(--paper);height:528px}
.single{width:408px}
.spread{width:820px;display:flex;border-radius:6px;overflow:hidden}
.spread .half{position:relative;width:410px;height:100%}
.spread .half+.half{border-left:1px solid var(--fold)}
.wide{width:588px;border-radius:0 6px 6px 0}
.rounded-left{border-radius:6px 0 0 6px}
.abs{position:absolute}
.title{font-family:"Montserrat",Arial,sans-serif;font-weight:800;font-size:8px;letter-spacing:.12em;display:flex;align-items:center;gap:6px}
.title .dots{font-weight:400;letter-spacing:.25em;color:var(--soft);font-size:8px}
.title-rule{border-bottom:1px solid var(--ink);padding-bottom:6px}
.label{font-family:"Montserrat",Arial,sans-serif;font-weight:400;font-size:5px;letter-spacing:.1em;text-transform:uppercase;color:var(--ink)}
.q{font-size:5px;letter-spacing:.06em;text-transform:uppercase;color:#444}
.lines{background:repeating-linear-gradient(to bottom,transparent 0 11px,var(--rule) 11px 12px)}
.lines-tight{background:repeating-linear-gradient(to bottom,transparent 0 9px,var(--rule) 9px 10px)}
.num{font-family:"Montserrat",Arial,sans-serif;font-size:6px;font-weight:700}
.box{background:var(--fill)}
.grid-cal{display:grid;grid-template-columns:repeat(7,1fr);grid-template-rows:repeat(5,1fr);border-top:1px solid var(--rule);border-left:1px solid var(--rule)}
.grid-cal span{border-right:1px solid var(--rule);border-bottom:1px solid var(--rule);font-size:4px;padding:2px;color:var(--soft)}
.tracker{display:grid;grid-template-columns:repeat(7,1fr);grid-template-rows:repeat(5,1fr);border-top:1px solid var(--rule);border-left:1px solid var(--rule)}
.tracker i{border-right:1px solid var(--rule);border-bottom:1px solid var(--rule)}
.check{width:5px;height:5px;border:1px solid var(--ink);display:inline-block;border-radius:50%;margin-right:5px;vertical-align:middle}
.row{display:flex;align-items:center}
.time{display:flex;align-items:flex-end;height:12.5px;border-bottom:1px solid var(--rule);font-size:4.5px;color:var(--soft);letter-spacing:.05em}
</style>
</head>
<body>

<!-- Daily page -->
<section class="page wide" style="left:600px;top:108px">
  <div class="abs title title-rule" style="left:24px;top:18px;width:540px">WEEK <span class="dots">. . . . . . . . . . . . . .</span>
    <svg style="margin-left:auto" width="9" height="9" viewBox="0 0 10 10"><path d="M1 5l3 3 5-7" fill="none" stroke="#1c1c1c" stroke-width="1.2"/></svg>
  </div>
  <div class="abs label" style="left:40px;top:50px">Priority tasks</div>
  <div class="abs" style="left:40px;top:62px;width:140px">
    <div class="row" style="height:22px;border-bottom:1px solid var(--rule)"><span class="num">1.</span></div>
    <div class="row" style="height:22px;border-bottom:1px solid var(--rule)"><span class="num">2.</span></div>
    <div class="row" style="height:22px;border-bottom:1px solid var(--rule)"><span class="num">3.</span></div>
  </div>
  <div class="abs label" style="left:40px;top:150px">Secondary tasks</div>
  <div class="abs lines" style="left:40px;top:160px;width:140px;height:132px"></div>
  <div class="abs" style="left:260px;top:50px;width:120px">
    <div class="time">6 AM</div><div class="time">7 AM</div><div class="time">8 AM</div><div class="time">9 AM</div>
    <div class="time">10 AM</div><div class="time">11 AM</div><div class="time">12 PM</div><div class="time">1 PM</div>
    <div class="time">2 PM</div><div class="time">3 PM</div><div class="time">4 PM</div><div class="time">5 PM</div>
    <div class="time">6 PM</div><div class="time">7 PM</div><div class="time">8 PM</div><div class="time">9 PM</div>
    <div class="time">10 PM</div><div class="time">11 PM</div><div class="time">12 AM</div><div class="time">1 AM</div>
    <div class="time">2 AM</div><div class="time">3 AM</div><div class="time">4 AM</div><div class="time">5 AM</div>
    <div class="time">NOTE</div><div class="time">NOTE</div>
  </div>
  <div class="abs" style="left:52px;top:446px;line-height:12px">
    <div class="label"><span class="check"></span>Personal activity</div>
    <div class="label"><span class="check"></span>Habit</div>
    <div class="label"><span class="check"></span>Weekly challenge</div>
  </div>
  <div class="abs label" style="left:440px;top:492px">Daily rating ★ . . . . .</div>
</section>

<!-- Notes + Weekly planning -->
<section class="page spread" style="left:192px;top:672px">
  <div class="half">
    <div class="abs title title-rule" style="left:22px;top:18px;width:366px">NOTES</div>
    <div class="abs lines" style="left:22px;top:40px;width:366px;height:468px"></div>
  </div>
  <div class="half">
    <div class="abs title title-rule" style="left:20px;top:18px;width:370px">WEEKLY PLANNING <span class="dots">. . . . . . . . . . . . .</span></div>
    <div class="abs label" style="left:20px;top:46px">Current challenge</div>
    <div class="abs" style="left:20px;top:56px;width:370px;height:22px;border:1px solid var(--rule)"></div>
    <div class="abs label" style="left:20px;top:88px">Current goals</div>
    <div class="abs" style="left:20px;top:96px;width:230px">
      <div class="row" style="height:20px;border-bottom:1px solid var(--rule)"><span class="num">1.</span></div>
      <div class="row" style="height:20px;border-bottom:1px solid var(--rule)"><span class="num">2.</span></div>
      <div class="row" style="height:20px;border-bottom:1px solid var(--rule)"><span class="num">3.</span></div>
    </div>
    <div class="abs" style="left:20px;top:170px;width:370px;height:330px;display:grid;grid-template-columns:1fr 1fr;grid-template-rows:repeat(3,1fr);gap:14px 10px">
      <div class="box label" style="padding:4px">Monday</div><div class="box label" style="padding:4px">Tuesday</div>
      <div class="box label" style="padding:4px">Wednesday</div><div class="box label" style="padding:4px">Thursday</div>
      <div class="box label" style="padding:4px">Friday</div><div class="box label" style="padding:4px">Weekend</div>
    </div>
  </div>
</section>

<!-- Weekly review + Month -->
<section class="page spread" style="left:192px;top:1248px">
  <div class="half">
    <div class="abs title title-rule" style="left:22px;top:18px;width:366px">WEEKLY REVIEW <span class="dots">. . . . . . . . . . . . .</span></div>
    <div class="abs q" style="left:22px;top:44px">What went well this week, and what did you learn?</div>
    <div class="abs lines" style="left:22px;top:52px;width:366px;height:48px"></div>
    <div class="abs q" style="left:22px;top:112px">Which goals moved forward, and what held them back?</div>
    <div class="abs lines" style="left:22px;top:120px;width:366px;height:48px"></div>
    <div class="abs q" style="left:22px;top:180px">What will you change or improve next week?</div>
    <div class="abs lines" style="left:22px;top:188px;width:366px;height:48px"></div>
    <div class="abs label" style="left:22px;top:266px">Notes</div>
    <div class="abs lines" style="left:22px;top:274px;width:366px;height:204px"></div>
    <div class="abs label" style="left:22px;top:492px">Daily statistics . . . . . . . .</div>
    <div class="abs label" style="left:330px;top:492px">Weekly avg</div>
  </div>
  <div class="half">
    <div class="abs title title-rule" style="left:20px;top:18px;width:370px">MONTH <span class="dots">. . . . . . . .</span></div>
    <div class="abs grid-cal" style="left:20px;top:52px;width:370px;height:200px">
      <span>M</span><span>T</span><span>W</span><span>T</span><span>F</span><span>S</span><span>S</span>
      <span></span><span></span><span></span><span></span><span></span><span></span><span></span>
      <span></span><span></span><span></span><span></span><span></span><span></span><span></span>
      <span></span><span></span><span></span><span></span><span></span><span></span><span></span>
      <span></span><span></span><span></span><span></span><span></span><span></span><span></span>
    </div>
    <div class="abs label" style="left:20px;top:270px">Notes</div>
    <div class="abs lines" style="left:20px;top:278px;width:370px;height:230px"></div>
  </div>
</section>

<!-- Goal pages -->
<section class="page spread" style="left:192px;top:1820px">
  <div class="half">
    <div class="abs title title-rule" style="left:22px;top:18px;width:366px">GOAL</div>
    <div class="abs label" style="left:22px;top:44px">Description</div>
    <div class="abs" style="left:22px;top:54px;width:366px;height:44px;border-bottom:1px solid var(--rule)"></div>
    <div class="abs label" style="left:22px;top:112px;width:366px;display:flex;justify-content:space-between">
      <span><span class="check"></span>Health</span><span><span class="check"></span>Career</span><span><span class="check"></span>Financial</span><span><span class="check"></span>Relationships</span><span><span class="check"></span>Personal</span>
    </div>
    <div class="abs q" style="left:22px;top:130px">Why is this goal important to you?</div>
    <div class="abs lines" style="left:22px;top:138px;width:366px;height:36px"></div>
    <div class="abs q" style="left:22px;top:196px">What steps will you take to reach this goal?</div>
    <div class="abs lines" style="left:22px;top:206px;width:366px;height:48px;border:1px solid var(--rule)"></div>
    <div class="abs q" style="left:22px;top:274px">How will you measure your progress?</div>
    <div class="abs lines" style="left:22px;top:282px;width:366px;height:24px"></div>
    <div class="abs label" style="left:22px;top:376px;font-weight:700">Habit tracker</div>
    <div class="abs label" style="left:22px;top:386px">Month 1</div>
    <div class="abs tracker" style="left:22px;top:394px;width:70px;height:56px"><i></i><i></i><i></i><i></i><i></i><i></i><i></i><i></i><i></i><i></i><i></i><i></i><i></i><i></i><i></i><i></i><i></i><i></i><i></i><i></i><i></i><i></i><i></i><i></i><i></i><i></i><i></i><i></i><i></i><i></i><i></i><i></i><i></i><i></i><i></i></div>
    <div class="abs label" style="left:150px;top:386px">Month 2</div>
    <div class="abs tracker" style="left:150px;top:394px;width:70px;height:56px"><i></i><i></i><i></i><i></i><i></i><i></i><i></i><i></i><i></i><i></i><i></i><i></i><i></i><i></i><i></i><i></i><i></i><i></i><i></i><i></i><i></i><i></i><i></i><i></i><i></i><i></i><i></i><i></i><i></i><i></i><i></i><i></i><i></i><i></i><i></i></div>
    <div class="abs label" style="left:278px;top:386px">Month 3</div>
    <div class="abs tracker" style="left:278px;top:394px;width:70px;height:56px"><i></i><i></i><i></i><i></i><i></i><i></i><i></i><i></i><i></i><i></i><i></i><i></i><i></i><i></i><i></i><i></i><i></i><i></i><i></i><i></i><i></i><i></i><i></i><i></i><i></i><i></i><i></i><i></i><i></i><i></i><i></i><i></i><i></i><i></i><i></i></div>
  </div>
  <div class="half">
    <div class="abs q" style="left:20px;top:28px">How will reaching this goal change your life?</div>
    <div class="abs lines" style="left:20px;top:36px;width:370px;height:48px"></div>
    <div class="abs q" style="left:20px;top:100px">Who can support you along the way?</div>
    <div class="abs lines" style="left:20px;top:108px;width:370px;height:48px"></div>
    <div class="abs" style="left:64px;top:172px;width:290px;height:110px;display:grid;grid-template-columns:1fr 1fr;border:1px solid var(--rule)">
      <div style="border-right:1px solid var(--rule)"><div class="label" style="text-align:center;padding:4px;border-bottom:1px solid var(--rule)">Possible obstacles</div><div class="lines-tight" style="height:90px"></div></div>
      <div><div class="label" style="text-align:center;padding:4px;border-bottom:1px solid var(--rule)">Possible solutions</div><div class="lines-tight" style="height:90px"></div></div>
    </div>
    <div class="abs label" style="left:20px;top:298px">Notes</div>
    <div class="abs lines" style="left:20px;top:306px;width:370px;height:200px"></div>
  </div>
</section>

<!-- Weekly challenges -->
<section class="page single rounded-left" style="left:192px;top:2388px">
  <div class="abs title title-rule" style="left:22px;top:18px;width:366px">WEEKLY CHALLENGES</div>
  <div class="abs" style="left:22px;top:40px;width:366px;height:250px;display:grid;grid-template-columns:1fr 80px;border-bottom:1px solid var(--rule)">
    <div class="lines" style="border-right:1px solid var(--rule)"></div>
    <div class="lines"></div>
  </div>
  <div class="abs label" style="left:22px;top:306px">Notes</div>
  <div class="abs lines" style="left:22px;top:314px;width:366px;height:196px"></div>
</section>

</body>
</html>
```